SEAFOOD PACKAGING (Products for consumer)

We are looking to create packaging for various seafood products such as octopus and squid. We plan to sell our products in upscale supermarkets.

We are specializing in cut octopus this time.

Please include our company logo. Also, please leave a transparent area so that customers can see the product inside.
Updates

We want to show what is inside, so a picture of the octopus is not required. We need something simple and sophisticated.

Target Market(s)

upscale store in US and ASIA

Industry/Entity Type

Fisheries dealer

Requirements
Must have
• Please include the attached logo,Blue one is preferred.Please leave a transparent part so that the contents of the product can be seen by the consumer.1. product name on packaging →CUT OCTOPUS,TAKO SASHIMI,Highest quality,Top quality etc... 3. What text information should be on the packaging →(It may be edited, but this is the image) The raw materials are caught in a very clean environment and processed in a modern factory with KVT certification. We are committed to additive-free products. 4. Packing size(cm/inch)→it will be about 19cm*22cm. 5. what kind of packaging do you use →PP or PA 6. dll →ai,jag
Nice to have
• https://plenvik.com/shots/4829173-Merulo-Prawn We need something simple and sophisticated like this one.
Should not have
• We want to show what is inside, so a picture of the octopus is not required. We need something simple and sophisticated.

```html
<!DOCTYPE html>
<html lang="en">
<head>
<meta charset="utf-8">
<title>Cut Octopus – Tako Sashimi Label</title>
<link rel="stylesheet" href="https://fonts.googleapis.com/css2?family=Antonio:wght@400;500&family=Courgette&family=Montserrat:wght@500;600&display=swap">
<style>
  :root {
    --backdrop: #d3e0e7;
    --sea-blue: #7fc1d8;
    --sea-blue-deep: #74b7cf;
    --label-white: #ffffff;
    --ink-navy: #2f6d9c;
    --ink-light: #7cbcd6;
    --star-blue: #4ba4c4;
    --window-tint: #cddfe7;
  }
  html, body {
    margin: 0;
    width: 1200px;
    height: 1000px;
    overflow: hidden;
    background: var(--backdrop);
  }
  .label {
    position: absolute;
    left: 220px;
    top: 62px;
    width: 760px;
    height: 876px;
    background: var(--label-white);
    box-shadow: 0 10px 30px rgba(40, 80, 110, 0.18);
    overflow: hidden;
  }
  .brand-panel {
    position: absolute;
    left: 0; top: 0;
    width: 341px; height: 100%;
    background: var(--sea-blue);
  }
  .edge-strip {
    position: absolute;
    right: 0; top: 0;
    width: 36px; height: 100%;
    background: var(--sea-blue);
  }
  .brand-mark {
    position: absolute;
    left: 0; top: 60px;
    width: 341px;
    text-align: center;
    color: var(--label-white);
  }
  .brand-dot {
    width: 70px; height: 70px;
    margin: 0 auto 22px;
    border-radius: 50%;
    background: var(--label-white);
  }
  .brand-name {
    font-family: "Antonio", sans-serif;
    font-weight: 500;
    font-size: 54px;
    letter-spacing: 6px;
    line-height: 1;
  }
  .brand-blurb {
    position: absolute;
    left: 74px; top: 326px;
    width: 210px;
    margin: 0;
    font-family: "Montserrat", sans-serif;
    font-weight: 500;
    font-size: 12.5px;
    line-height: 1.6;
    color: var(--label-white);
  }
  .wave-band {
    position: absolute;
    left: 0; top: 651px;
    width: 341px; height: 225px;
    background: linear-gradient(180deg, var(--sea-blue) 0%, var(--sea-blue-deep) 100%);
  }
  .product-window {
    position: absolute;
    left: 39px; top: 430px;
    width: 271px; height: 392px;
    background: var(--window-tint);
  }
  .rating {
    position: absolute;
    left: 481px; top: 68px;
    display: flex; gap: 6px;
  }
  .tagline {
    position: absolute;
    left: 380px; top: 98px;
    width: 320px;
    margin: 0;
    text-align: center;
    font-family: "Courgette", cursive;
    font-size: 42px;
    font-weight: 400;
    line-height: 1;
    color: var(--ink-navy);
  }
  .product-name,
  .product-subname {
    position: absolute;
    margin: 0;
    writing-mode: vertical-rl;
    transform: rotate(180deg);
    white-space: nowrap;
    line-height: 1;
  }
  .product-name {
    left: 382px; top: 209px;
    height: 536px;
    font-family: "Antonio", sans-serif;
    font-weight: 400;
    font-size: 98px;
    letter-spacing: 1px;
    color: var(--ink-navy);
    text-align: center;
  }
  .product-subname {
    left: 514px; top: 209px;
    height: 414px;
    font-family: "Courgette", cursive;
    font-weight: 400;
    font-size: 58px;
    color: var(--ink-light);
    text-align: center;
  }
  .claims {
    position: absolute;
    left: 504px; top: 670px;
    width: 183px; height: 90px;
    box-sizing: border-box;
    border: 2px solid var(--ink-light);
    padding: 16px 0 0 10px;
    margin: 0;
    list-style: none;
    font-family: "Montserrat", sans-serif;
    font-weight: 600;
    font-size: 11.5px;
    line-height: 1.45;
    color: var(--ink-navy);
  }
  .net-weight {
    position: absolute;
    left: 341px; top: 820px;
    width: 383px;
    margin: 0;
    text-align: center;
    font-family: "Antonio", sans-serif;
    font-weight: 400;
    font-size: 30px;
    letter-spacing: 0.5px;
    color: var(--ink-navy);
  }
</style>
</head>
<body>
  <main class="label">
    <section class="brand-panel">
      <div class="brand-mark">
        <div class="brand-dot"></div>
        <div class="brand-name">MARLO</div>
      </div>
      <p class="brand-blurb">Lorem Lorem ipsum dolor sit amet, consectetuer adipiscing elit, sed diam nonummy nibh</p>
      <div class="wave-band" role="img" aria-label="Fine wavy sea-line pattern in soft blue"></div>
      <div class="product-window" aria-label="Transparent window showing the product"></div>
    </section>

    <div class="edge-strip"></div>

    <svg class="rating" width="124" height="20" viewBox="0 0 124 20" aria-label="Five stars">
      <g fill="var(--star-blue)">
        <polygon points="10,1 12.6,7 19,7.4 14,11.6 15.6,18 10,14.5 4.4,18 6,11.6 1,7.4 7.4,7"/>
        <polygon transform="translate(26 0)" points="10,1 12.6,7 19,7.4 14,11.6 15.6,18 10,14.5 4.4,18 6,11.6 1,7.4 7.4,7"/>
        <polygon transform="translate(52 0)" points="10,1 12.6,7 19,7.4 14,11.6 15.6,18 10,14.5 4.4,18 6,11.6 1,7.4 7.4,7"/>
        <polygon transform="translate(78 0)" points="10,1 12.6,7 19,7.4 14,11.6 15.6,18 10,14.5 4.4,18 6,11.6 1,7.4 7.4,7"/>
        <polygon transform="translate(104 0)" points="10,1 12.6,7 19,7.4 14,11.6 15.6,18 10,14.5 4.4,18 6,11.6 1,7.4 7.4,7"/>
      </g>
    </svg>

    <p class="tagline">highest quality</p>
    <h1 class="product-name">CUT OCTOPUS</h1>
    <h2 class="product-subname">Tako sashimi</h2>

    <ul class="claims">
      <li>ADDITIVE-FREE PRODUCTS</li>
      <li>FRESH FROM THE SEA</li>
      <li>KEEP FROZEN</li>
    </ul>

    <p class="net-weight">NET WT 1LBS KEEP FROZEN</p>
  </main>
</body>
</html>
```